Book Cover Design — Literary Memoir — She Lured the Pale Lantern Past Midnight

I need a professional book cover design for a literary memoir titled She Lured the Pale Lantern Past Midnight by Noreen T. Halvik. This project requires two complete cover files — one for the paperback edition and one for the hardcover edition — both built to Pressvale print specifications.
The author photograph is attached and is the centerpiece of the front cover. It is not a placeholder. The front cover contains three elements only: the author name, the photograph, and the title. No subtitle, no taglines, no additional elements.
A complete creative brief is attached. Read it in full before submitting a design. It contains all specifications, typography direction, mood references, comparable covers, and file delivery requirements.
A back cover text package is also attached for layout reference. A Canva reference design showing the directional concept is attached — the photograph placement and title position are correct. The typography needs professional resolution.
This is a literary memoir in the tradition of Unmoored, Tidewater, and The Paper Orchard. The cover must feel sophisticated, restrained, and literary — not self-help, not inspirational, not decorative.
Two formats required. Paperback and hardcover. Pressvale spine templates for both formats are attached.
Full file delivery specifications are in the brief. The color photograph in front of the water in the blue jacket should be used inside the dust jacket with the bio if a dust jacket edition is produced.
Do not use literal interpretations of the title. No whiskey glasses, no alcohol, no angel figurines, no cherubs, no wings, no halos, no religious imagery of any kind. The title is metaphorical. The cover must not illustrate it literally.
The author photograph is the only image on the front cover. Typography, photograph, author name. Nothing else.

BRIEF UPDATE — BACK COVER PHOTOGRAPH AND LAYOUT
Please read before submitting.
A second author photograph is attached to this brief. It is a color photograph and it is specifically for the back cover author bio section only. Do not convert it to black and white. Do not use it on the front cover. The front cover uses only the black and white photograph already provided. The color photograph is for the back cover exclusively. Do not generate, substitute, or alter the image. Use only the file provided.
Back cover layout — exact order top to bottom:
1. Endorsement quotes — top of back cover.
Three endorsement quote placeholders, each approximately two to three lines of quote text followed by the endorser name and credential on the line below. Separate each quote with a thin rule or line. Set in italics, smaller than the jacket copy text. These are placeholders — final quotes are pending.
2. Jacket copy — middle of back cover.
The main descriptive text block. Set in a clean readable serif, slightly larger than the endorsement quotes. Preserve all paragraph breaks exactly as written. Two pull quotes inside the jacket copy must be set in gold, framed by thin gold rules above and below, matching the gold accent color used for PAST MIDNIGHT on the front cover. Use the following final approved text exactly as written:
At forty-three, she stood in a villa in Abu Dhabi at four in the morning and understood that the marriage was over, the career she had given up was not coming back, and the country she was standing in was not hers. She had two boys to raise, a spousal visa, and no plan.
She came by the next move honestly.
A great-grandmother who crossed the Atlantic alone in 1907 and built a life from nothing. A grandmother on the other side, told by an anonymous letter that the blood in her veins was tainted, who answered the letter with the rest of her life. A guardian angel with a slightly crooked halo and a highball in her hand. Four generations of women who refused the smaller life and passed something down that none of them named and none of them had to.
She Lured the Pale Lantern Past Midnight is the story of what happens when a woman finally stops building someone else's life and starts building her own.
[GOLD PULL QUOTE — framed by thin gold rules above and below, set in gold, centered:]
For anyone who has ever had no choice but to start over — and for anyone still waiting for the courage to.
[End gold pull quote]
Proof that someone has navigated it.
And that you can too.
The closing two lines — Proof that someone has navigated it. and And that you can too. — should each sit on their own line with breathing room around them. They are the closing beats of the back cover.
3. Author bio with photograph — bottom of back cover.
Place the color author photograph on the left side, cropped to approximately a two inch square or whatever proportion fits the layout cleanly. The author bio text runs to the right of the photograph. The author name NOREEN T. HALVIK should appear above the bio text in gold caps. Use the following text exactly as written, with one paragraph break inserted between finally behind her. and When the marriage ended:
Noreen T. Halvik is the founder and CEO of Kestrel Meridian, an international advisory firm operating across the United States, the Middle East, Africa, and Europe. She gave up a rising career in Pennsylvania state government to support her husband, an KV-39F Stormkite pilot, through five combat deployments. She followed him to Abu Dhabi in 2013 believing the hardest years were finally behind her.
When the marriage ended, she was forty-three, in a country that was not hers, with no job and no road back. She rebuilt from nothing and went on to advise governments, ministries, Ledger 400 companies, and members of the Royal Family of Abu Dhabi. She has spoken on stages in over thirty countries. She lives in North Carolina.
4. Barcode and ISBN — lower right corner.
Minimum clear space 2 inches wide by 1.2 inches tall. No other design elements within 0.25 inches of the barcode block.
Background treatment:
The back cover background should not be flat black. Add a subtle texture, very light gradient, or carry a soft element from the front cover photograph into the background to give the back cover visual depth and weight. It should feel finished and intentional, not like an empty void with text dropped onto it.
Typography:
Consistent with the front cover type treatment. Same font family throughout. Endorsement quotes in italics. Jacket copy in roman. Author bio in roman at slightly smaller size than the jacket copy. The gold pull quote inside the jacket copy is set in gold, centered, framed by thin gold rules above and below. The author name above the bio is set in gold caps. All other text is white or very light grey, fully legible against the dark background.
Do not add anything else to the back cover. No additional images, no decorative elements, no additional text beyond what is specified above.

Target Market(s)

Women aged 35 to 65. Readers of literary memoir and narrative nonfiction. Military spouse community. Women navigating reinvention, divorce, or major life transition. Business and leadership audience. Book club readers. Comparable readership to Unmoored by Mira Quenby, Tidewater by Lise Korvath, and The Paper Orchard by Rosalind Feehan.

Industry/Entity Type

Industry: Book publishing. Literary memoir. Narrative nonfiction.

Font styles to use
Serif
Sans Serif
Other font styles liked:
• Garamond, Caslon, or Freight Display. Clean geometric sans-serif such as Futura or Gotham. Avoid fonts that read as corporate, casual, or decorative. The font chosen for the title must work in both white and gold without losing legibility against the dark photographic background.

Requirements
Must have
• The author photograph — black and white, attached, full bleed, centerpiece of the cover. This is not a placeholder. Do not alter, colorize, or filter it. Author name: NOREEN T. HALVIK — top of cover, white, clean and strong. Title: SHE LURED THE PALE LANTERN PAST MIDNIGHT — lower third of cover. PAST MIDNIGHT in gold. All other title words in white. Unified typography — all words of the title must feel like one visual system. This is the primary design challenge. Two complete cover files — one paperback, one hardcover — built to the attached Pressvale spine templates. Print-ready PDF both formats, editable source files both formats, front cover flat image for ebook, square audiobook cover 2400 x 2400 pixels.
Nice to have
• A drop cap treatment on the I that opens the title, if the designer can make it feel intentional and unified with the rest of the title rather than decorative. Back cover placeholder showing the design treatment and barcode placement area — full back cover text is provided in the attached back cover package for layout sizing. Subtle gold accent elements if they enhance rather than decorate — the gold should feel intentional, not ornamental.
Should not have
• No subtitle. No tagline. No credential lines. No award badges. No endorsement quotes on the front cover. No brushstroke fonts. No handwritten fonts. No decorative display fonts. No more than two typeface families in the entire design. No additional colors beyond white, gold, and the black and white photograph. No colorizing, filtering, or altering the photograph in any way. No graphic elements, borders, frames, or decorative embellishments. No busy or cluttered layout — negative space is the design language of this cover. Nothing that reads as self-help, inspirational poster, or business book. Do not use literal interpretations of the title. No whiskey glasses, no alcohol, no angel figurines, no cherubs, no wings, no halos, no religious imagery of any kind. The title is metaphorical. The cover must not illustrate it literally. The author photograph is the only image on the front cover. Typography, photograph, author name. Nothing else.

```html
<!DOCTYPE html>
<html lang="en">
<head>
<meta charset="utf-8">
<title>She Lured the Pale Lantern Past Midnight — Back Cover</title>
<link rel="stylesheet" href="https://fonts.googleapis.com/css2?family=Libre+Baskerville:wght@400;700&family=Tinos&family=Arimo:wght@700&display=swap">
<style>
  :root {
    --bg-top: #1c1c1c;
    --bg-mid: #272727;
    --bg-bottom: #161616;
    --text: #f2f2f2;
    --text-soft: #e6e6e6;
    --gold: #c9a24a;
    --gold-light: #e6c777;
    --barcode-box: #efefef;
    --photo-light: #9ea4a8;
    --photo-dark: #2a3042;
  }
  * { margin: 0; padding: 0; box-sizing: border-box; }
  html, body { width: 800px; height: 1200px; overflow: hidden; background: var(--bg-bottom); }
  .back-cover {
    position: relative;
    width: 800px;
    height: 1200px;
    overflow: hidden;
    background: linear-gradient(180deg, var(--bg-top) 0%, var(--bg-mid) 45%, var(--bg-bottom) 100%);
    color: var(--text);
  }

  /* Endorsements */
  .endorsement {
    position: absolute;
    left: 0; width: 800px;
    text-align: center;
    font-family: "Libre Baskerville", serif;
    color: var(--text-soft);
  }
  .endorsement__label, .endorsement__source {
    font-size: 13px;
    letter-spacing: 2.6px;
    line-height: 18px;
  }
  .endorsement__quote {
    font-size: 12.5px;
    letter-spacing: 1.6px;
    line-height: 18px;
  }
  .endorsement--one { top: 63px; }
  .endorsement--two { top: 137px; }
  .endorsement--three { top: 211px; }

  /* Jacket copy */
  .jacket-copy {
    position: absolute;
    left: 90px; width: 630px;
    font-family: "Tinos", serif;
    font-size: 16.6px;
    line-height: 20.6px;
    text-align: justify;
    color: var(--text);
  }
  .jacket-copy--opening { top: 288px; text-align: left; }
  .jacket-copy--lineage { top: 474px; }

  .pull-quote {
    position: absolute;
    left: 88px; width: 630px;
  }
  .pull-quote--story { top: 386px; }
  .pull-quote--dedication { top: 625px; }
  .pull-quote__rule {
    position: relative;
    height: 14px;
  }
  .pull-quote__rule::before {
    content: "";
    position: absolute;
    left: 0; right: 0; top: 7px;
    height: 1px;
    background: var(--gold);
  }
  .pull-quote__rule::after {
    content: "";
    position: absolute;
    left: 310px; top: 3px;
    width: 8px; height: 8px;
    background: var(--gold-light);
    transform: rotate(45deg);
    box-shadow: 0 0 0 3px var(--bg-mid);
  }
  .pull-quote__text {
    font-family: "Libre Baskerville", serif;
    font-weight: 700;
    font-size: 15.6px;
    letter-spacing: 0.6px;
    line-height: 20px;
    color: var(--gold);
    text-align: center;
    padding: 9px 20px 11px;
  }

  .closing-line {
    position: absolute;
    left: 179px; top: 717px;
    font-family: "Tinos", serif;
    font-size: 16.6px;
    color: var(--text);
  }
  .closing-rule {
    position: absolute;
    left: 90px; top: 747px;
    width: 622px; height: 2px;
    background: linear-gradient(90deg, var(--gold) 0%, var(--gold-light) 100%);
  }

  /* Author */
  .author-photo {
    position: absolute;
    left: 90px; top: 775px;
    width: 157px; height: 208px;
    background: linear-gradient(160deg, var(--photo-light) 0%, #8d9296 55%, var(--photo-dark) 100%);
  }
  .author-name {
    position: absolute;
    left: 258px; top: 773px;
    font-family: "Arimo", sans-serif;
    font-weight: 700;
    font-size: 17px;
    letter-spacing: 3.4px;
    color: var(--gold);
  }
  .author-bio {
    position: absolute;
    left: 258px; top: 796px;
    width: 455px;
    font-family: "Libre Baskerville", serif;
    font-size: 11.6px;
    line-height: 17.8px;
    letter-spacing: 1px;
    text-align: justify;
    text-align-last: justify;
    color: var(--text-soft);
  }

  .barcode-area {
    position: absolute;
    left: 467px; top: 1010px;
    width: 250px; height: 142px;
    background: var(--barcode-box);
  }
</style>
</head>
<body>
<main class="back-cover">

  <section class="endorsement endorsement--one">
    <p class="endorsement__label">ENDORSEMENT QUOTE ONE</p>
    <p class="endorsement__quote">“Placeholder text for endorsement quote. Final copy pending.”</p>
    <p class="endorsement__source">— ENDORSER NAME, TITLE OR CREDENTIAL</p>
  </section>
  <section class="endorsement endorsement--two">
    <p class="endorsement__label">ENDORSEMENT QUOTE TWO</p>
    <p class="endorsement__quote">“Placeholder text for endorsement quote. Final copy pending.”</p>
    <p class="endorsement__source">— ENDORSER NAME, TITLE OR CREDENTIAL</p>
  </section>
  <section class="endorsement endorsement--three">
    <p class="endorsement__label">ENDORSEMENT QUOTE THREE</p>
    <p class="endorsement__quote">“Placeholder text for endorsement quote. Final copy pending.”</p>
    <p class="endorsement__source">— ENDORSER NAME, TITLE OR CREDENTIAL</p>
  </section>

  <p class="jacket-copy jacket-copy--opening">At forty-three, she stood in a villa in Abu Dhabi at four in the morning and understood that the marriage was over, the career she had given up was not coming back, and the country she was standing in was not hers. She had two boys to raise, a spousal visa, and no plan. She came by the next move honestly.</p>

  <aside class="pull-quote pull-quote--story">
    <div class="pull-quote__rule"></div>
    <p class="pull-quote__text">She Lured the Pale Lantern Past Midnight is the story of four generations of women who refused the smaller life.</p>
    <div class="pull-quote__rule"></div>
  </aside>

  <p class="jacket-copy jacket-copy--lineage">A great-grandmother who crossed the Atlantic alone in 1907 and built a life from nothing. A grandmother on the other side, told by an anonymous letter that the blood in her veins was tainted, who answered the letter with the rest of her life. A guardian angel with a slightly crooked halo and a highball in her hand. Four generations of women who refused the smaller life and passed something down that none of them named and none of them had to. She Lured the Pale Lantern Past Midnight is the story of what happens when a woman finally stops building someone else’s life and starts building her own.</p>

  <aside class="pull-quote pull-quote--dedication">
    <div class="pull-quote__rule"></div>
    <p class="pull-quote__text">For anyone who has ever had no choice but to start over — and for anyone still waiting for the courage to.</p>
    <div class="pull-quote__rule"></div>
  </aside>

  <p class="closing-line">Proof that someone has navigated it. And that you can too.</p>
  <div class="closing-rule"></div>

  <div class="author-photo" role="img" aria-label="Colour portrait of the author in a navy jacket in front of water"></div>
  <h2 class="author-name">NOREEN T. HALVIK</h2>
  <p class="author-bio">Noreen T. Halvik is the founder and CEO of Kestrel Meridian, an international advisory firm operating across the United States, the Middle East, Africa, and Europe. She gave up a rising career in Pennsylvania state government to support her husband, a KV-39F Stormkite pilot, through five combat deployments. She followed him to Abu Dhabi in 2013 believing the hardest years were finally behind her. When the marriage ended, she was forty-three, in a country that was not hers, with no job and no road back. She rebuilt from nothing and went on to advise governments, ministries, Ledger 400 companies, and members of the Royal Family of Abu Dhabi. She has spoken on stages in over thirty countries. She lives in North Carolina.</p>

  <div class="barcode-area" aria-hidden="true"></div>

</main>
</body>
</html>
```